Australian residential property business needs a business card design

I need a business card design for my new business 'Meadow Estate Partners'. The business will involve house purchases, land development sites, renovation projects, sub-divisions etc. I will be buying property from motivated vendors and working with property investors. I will deal with a wide range of people working in the residential property market including real estate agents, councils, tradespeople, banks, home owners, etc.

I would like something simple, not flashy, but a little bit unique. The colours should be in line with my logo. The business card needs to be professional. I would like something memorable, but not 'busy' or too bright. Not boring. Modern ok.

Target Market(s)

Home owners looking to sell their property, real estate agents, tradespeople (e.g. plumbers, builders, electricians etc), property investors, local councils, and anyone else involved in the residential property industry

Industry/Entity Type

Business

Contact Information for Business Card

I need to include my business name/logo, my name, my title, a PO Box number/address, a mobile number, and an email address.

Font styles to use
Serif

Requirements
Must have
• My business card details listed above.

```html
<!DOCTYPE html>
<html lang="en">
<head>
<meta charset="utf-8">
<title>Meadow Estate Partners – Business Card</title>
<link rel="stylesheet" href="https://fonts.googleapis.com/css2?family=Mulish:wght@400;700;800&display=swap">
<style>
  :root {
    --backdrop: #eceeee;
    --card: #ffffff;
    --green: #0a8f0a;
    --orange: #f6a824;
    --ink: #3f3f3f;
    --white: #ffffff;
  }
  * { margin: 0; padding: 0; box-sizing: border-box; }
  html, body {
    width: 1200px;
    height: 753px;
    overflow: hidden;
    background: var(--backdrop);
    font-family: "Mulish", "Century Gothic", sans-serif;
  }
  .card {
    position: absolute;
    left: 124px;
    top: 130px;
    width: 929px;
    height: 553px;
  }
  .card-shape {
    position: absolute;
    inset: 0;
    width: 929px;
    height: 553px;
  }
  .card-shape .base { fill: var(--card); }
  .card-shape .accent-stripe { fill: var(--orange); }
  .card-shape .footer-band { fill: var(--green); }

  .person-name {
    position: absolute;
    left: 105px;
    top: 108px;
    font-size: 34px;
    font-weight: 800;
    color: var(--green);
    line-height: 1;
  }
  .person-title {
    position: absolute;
    left: 105px;
    top: 158px;
    font-size: 31px;
    font-weight: 400;
    color: var(--ink);
    line-height: 1;
  }
  .contact-line {
    position: absolute;
    left: 105px;
    display: flex;
    align-items: center;
    gap: 14px;
    font-size: 26px;
    color: var(--ink);
    line-height: 1;
  }
  .contact-line svg { width: 28px; height: 28px; flex: none; }
  .contact-line svg .icon { fill: var(--green); }
  .contact-line svg .icon-stroke { fill: none; stroke: var(--green); stroke-width: 2.4; stroke-linejoin: round; }
  .contact-phone { top: 234px; }
  .contact-email { top: 277px; }
  .contact-address { top: 339px; }

  .brand {
    position: absolute;
    left: 520px;
    top: 180px;
    width: 400px;
    display: flex;
    align-items: center;
    justify-content: center;
    gap: 12px;
  }
  .brand-dot {
    width: 22px;
    height: 22px;
    border-radius: 50%;
    background: var(--orange);
    flex: none;
  }
  .brand-name {
    font-size: 29px;
    font-weight: 800;
    color: var(--green);
    white-space: nowrap;
  }

  .tagline {
    position: absolute;
    left: 0;
    width: 929px;
    top: 470px;
    text-align: center;
    font-size: 34px;
    font-weight: 700;
    letter-spacing: 5px;
    color: var(--white);
    line-height: 1;
  }
</style>
</head>
<body>
  <div class="card">
    <svg class="card-shape" viewBox="0 0 929 553" aria-hidden="true">
      <defs>
        <clipPath id="card-outline">
          <path d="M0,140 A140,140 0 0 1 140,0 H929 V413 A140,140 0 0 1 789,553 H0 Z"/>
        </clipPath>
      </defs>
      <g clip-path="url(#card-outline)">
        <rect class="base" x="0" y="0" width="929" height="553"/>
        <path class="accent-stripe" d="M0,407 H690 C820,407 915,385 929,284 V553 H0 Z"/>
        <path class="footer-band" d="M0,421 H690 C830,421 920,395 929,302 V553 H0 Z"/>
      </g>
    </svg>

    <div class="brand">
      <span class="brand-dot"></span>
      <span class="brand-name">Meadow Estate Partners</span>
    </div>

    <h1 class="person-name">Your Name</h1>
    <p class="person-title">Position</p>

    <p class="contact-line contact-phone">
      <svg viewBox="0 0 24 24" aria-hidden="true">
        <path class="icon" d="M6.6 3.2c.5-.4 1.2-.3 1.6.2l2.2 3c.4.5.3 1.2-.1 1.6l-1.3 1.2c.9 2 2.6 4 4.6 5.2l1.3-1.2c.5-.4 1.2-.4 1.6 0l2.9 2.3c.5.4.6 1.1.2 1.6l-1.5 1.9c-.6.7-1.6 1-2.5.7C9.8 17.9 5.6 13.4 4.3 7.6c-.2-.9.1-1.8.8-2.4z"/>
      </svg>
      <span>123-456-7888</span>
    </p>
    <p class="contact-line contact-email">
      <svg viewBox="0 0 24 24" aria-hidden="true">
        <rect class="icon-stroke" x="2.5" y="5.5" width="19" height="13"/>
        <polyline class="icon-stroke" points="2.5,5.5 12,13 21.5,5.5"/>
      </svg>
      <span>name@companyname.com</span>
    </p>
    <p class="contact-line contact-address">
      <svg viewBox="0 0 24 24" aria-hidden="true">
        <path class="icon" d="M12 2c-4 0-7 3-7 7 0 5 7 13 7 13s7-8 7-13c0-4-3-7-7-7zm0 9.6a2.6 2.6 0 1 1 0-5.2 2.6 2.6 0 0 1 0 5.2z"/>
      </svg>
      <span>PO Box, Address</span>
    </p>

    <p class="tagline">Your Tagline Here</p>
  </div>
</body>
</html>
```